fully distributed
Project: fully distributed
fully distributed  - Information Technology
Creative Brief
Use specific fonts
calibri
Simple
Doug Pelliver
CMO
482 Corwin St , Floor 6 New York NY 10019
doug.pelliver@tulvaro.com
logo only
marcste marcste
on 18 and 19 can you fade the grey a litle so it just looks like a faint color
Xpert Xpert
Sure Sir.
we like some of yr designs can u try the design of 17 with the physical layout of card 2
like what you have started will check each one out
thanks we are looking for stationary too
please add fax number 1 800 937 2584

```html
<!DOCTYPE html>
<html lang="en">
<head>
<meta charset="utf-8">
<title>Tulvaro Stationery</title>
<link href="https://fonts.googleapis.com/css2?family=Carlito:wght@400;700&display=swap" rel="stylesheet">
<style>
  :root{
    --bg:#ececec;
    --paper:#ffffff;
    --ink:#2b2b2b;
    --soft:#8a8a8a;
    --red:#d2323a;
    --black:#1c1c1c;
  }
  *{margin:0;padding:0;box-sizing:border-box}
  html,body{width:1200px;height:937px;overflow:hidden;background:var(--bg);font-family:"Carlito",Calibri,sans-serif;color:var(--ink)}
  .canvas{position:relative;width:1200px;height:937px}
  .sheet{position:absolute;background:var(--paper);overflow:hidden}
  .swoosh{position:absolute;left:0;bottom:0;width:100%;display:block}

  .brand{display:flex;align-items:center;gap:5px;font-weight:700;color:var(--ink);line-height:1;white-space:nowrap}
  .brand .dot{display:inline-block;border-radius:50%;background:var(--ink)}

  /* letterhead */
  .letterhead{left:177px;top:63px;width:420px;height:557px}
  .letterhead .brand{position:absolute;left:32px;top:44px;font-size:24px}
  .letterhead .brand .dot{width:7px;height:7px}
  .letterhead .contact{position:absolute;right:30px;top:40px;font-size:5px;line-height:1.5;color:var(--soft)}
  .letter{position:absolute;left:34px;top:118px;width:340px;font-size:5.5px;line-height:1.6;color:#555}
  .letter p{margin-bottom:9px}
  .letter .sign{font-size:11px;color:#333;margin:4px 0}

  /* folder */
  .folder{left:633px;top:38px;width:467px;height:582px}
  .folder .brand{position:absolute;left:50%;top:255px;transform:translateX(-50%);font-size:58px}
  .folder .brand .dot{width:13px;height:13px}

  /* business cards */
  .card{width:194px;height:94px}
  .card-front{left:46px;top:653px}
  .card-back{left:46px;top:780px}
  .card .brand{font-size:16px}
  .card .brand .dot{width:5px;height:5px}
  .card-front .brand{position:absolute;left:12px;top:16px}
  .card-front .divider{position:absolute;left:104px;top:12px;width:1px;height:42px;background:#ddd}
  .card-front .details{position:absolute;left:110px;top:11px;font-size:4.2px;line-height:1.45;color:#555}
  .card-front .details strong{font-size:5.5px;color:var(--ink)}
  .card-back .brand{position:absolute;left:50%;top:40px;transform:translateX(-50%)}

  /* envelopes */
  .env-front{left:266px;top:670px;width:448px;height:203px}
  .env-front .brand{position:absolute;left:12px;top:16px;font-size:17px}
  .env-front .brand .dot{width:5px;height:5px}
  .env-back{left:740px;top:670px;width:425px;height:203px}
  .env-back .flap{position:absolute;left:0;top:0;width:100%;height:100%;display:block}
  .env-back .web{position:absolute;left:0;top:16px;width:100%;text-align:center;color:#fff;font-size:11px;letter-spacing:3px}
</style>
</head>
<body>
<main class="canvas">

  <section class="sheet letterhead">
    <div class="brand">tulvaro<span class="dot"></span></div>
    <div class="contact">482 Corwin St , Floor 6<br>New York NY 10019<br>1 800 937 2584<br>doug.pelliver@tulvaro.com</div>
    <div class="letter">
      <p>July 8, 2024</p>
      <p>Jane Doe<br>100 Main Street, Suite 1, New York</p>
      <p>Dear Jane,</p>
      <p>Thank you for your interest in our fully distributed solution. Our team delivers secure, scalable systems that keep every office connected and every project moving forward without delay.</p>
      <p>We look forward to working with you and will follow up shortly with a detailed proposal for your review.</p>
      <p>Please contact us with any questions about scheduling, pricing or support.</p>
      <p>Best regards,</p>
      <p class="sign">D. Pelliver</p>
      <p>Doug Pelliver<br>CMO</p>
    </div>
    <svg class="swoosh" viewBox="0 0 420 70" height="70" preserveAspectRatio="none" aria-hidden="true">
      <path d="M0,18 Q200,-6 420,14" fill="none" stroke="var(--red)" stroke-width="2.5"/>
      <path d="M0,30 Q200,4 420,22 L420,70 L0,70 Z" fill="var(--black)"/>
    </svg>
  </section>

  <section class="sheet folder">
    <div class="brand">tulvaro<span class="dot"></span></div>
    <svg class="swoosh" viewBox="0 0 467 80" height="80" preserveAspectRatio="none" aria-hidden="true">
      <path d="M0,20 Q230,-6 467,16" fill="none" stroke="var(--red)" stroke-width="3"/>
      <path d="M0,32 Q230,4 467,26 L467,80 L0,80 Z" fill="var(--black)"/>
    </svg>
  </section>

  <section class="sheet card card-front">
    <div class="brand">tulvaro<span class="dot"></span></div>
    <div class="divider"></div>
    <div class="details">
      <strong>Doug Pelliver</strong><br>CMO<br>T 1 800 937 2584<br>F 1 800 937 2584<br>doug.pelliver@tulvaro.com<br>482 Corwin St , Floor 6<br>New York NY 10019
    </div>
    <svg class="swoosh" viewBox="0 0 194 24" height="24" preserveAspectRatio="none" aria-hidden="true">
      <path d="M0,7 Q100,-2 194,5" fill="none" stroke="var(--red)" stroke-width="1.5"/>
      <path d="M0,11 Q100,2 194,9 L194,24 L0,24 Z" fill="var(--black)"/>
    </svg>
  </section>

  <section class="sheet card card-back">
    <div class="brand">tulvaro<span class="dot"></span></div>
  </section>

  <section class="sheet env-front">
    <div class="brand">tulvaro<span class="dot"></span></div>
    <svg class="swoosh" viewBox="0 0 448 50" height="50" preserveAspectRatio="none" aria-hidden="true">
      <path d="M0,14 Q220,-4 448,10" fill="none" stroke="var(--red)" stroke-width="2"/>
      <path d="M0,22 Q220,3 448,17 L448,50 L0,50 Z" fill="var(--black)"/>
    </svg>
  </section>

  <section class="sheet env-back">
    <svg class="flap" viewBox="0 0 425 203" preserveAspectRatio="none" aria-hidden="true">
      <rect x="0" y="0" width="425" height="48" fill="var(--black)"/>
      <path d="M0,48 L212,120 L425,48" fill="#f6f6f6" stroke="#e0e0e0" stroke-width="1"/>
      <path d="M0,50 Q212,34 425,50" fill="none" stroke="var(--red)" stroke-width="2"/>
    </svg>
    <div class="web">www.tulvaro.com</div>
  </section>

</main>
</body>
</html>
```